Flyer for family counseling

For my family counseling I'm looking for a design for flyers. Important is not only the appearance of the flyer, but also the content design. All important contents can be found on my website: www.brigitte-volkanter.at The following items should NOT appear on the flyer: - constellation work - bereavement and palliative work My logo should definitely be on the flyer. Source files are available.

Target Market(s)

Families, individuals, children, couples in need of psychological support.

Colors

Designer to choose colors to be used in the design.

Requirements
Must have
• My logo - source files available Website and contact data Recognition value from website to flyer and vice versa
Should not have
• Mention of the constellation work and mourning and palliative work not desired.

```html
<!DOCTYPE html>
<html lang="de">
<head>
<meta charset="utf-8">
<title>Familienberatung Lindenhof – Flyer</title>
<link href="https://fonts.googleapis.com/css2?family=Didact+Gothic&family=Montserrat:wght@600;700&display=swap" rel="stylesheet">
<style>
  :root {
    --teal: #3f9c92;
    --blue: #2f64ad;
    --ink: #3b3b3b;
    --muted: #6d6d6d;
    --paper: #ffffff;
    --row-grey: #e4e4e4;
    --divider: #c9c9c9;
    --backdrop: #e9e9e7;
    --photo-warm-a: #e9cfa9;
    --photo-warm-b: #b88a62;
  }
  * { box-sizing: border-box; margin: 0; padding: 0; }
  html, body { width: 1200px; height: 984px; overflow: hidden; }
  body {
    background: var(--backdrop);
    font-family: "Didact Gothic", "Century Gothic", sans-serif;
    color: var(--ink);
  }
  .flyer {
    position: absolute;
    left: 260px; top: 11px;
    width: 680px; height: 962px;
    background: var(--paper);
    box-shadow: 0 4px 18px rgba(0,0,0,.18);
    overflow: hidden;
  }
  .brand { position: absolute; top: 18px; left: 0; width: 100%; text-align: center; }
  .brand-mark {
    display: block; width: 34px; height: 34px; margin: 0 auto 8px;
    border-radius: 50%; background: var(--teal);
  }
  .brand-name { font-size: 16px; letter-spacing: 1.5px; color: var(--blue); text-transform: uppercase; line-height: 1.2; }
  .brand-sub { margin-top: 3px; font-size: 8px; letter-spacing: 5px; color: var(--blue); text-transform: uppercase; }
  .photo { background: linear-gradient(135deg, var(--photo-warm-a), var(--photo-warm-b)); }
  .hero {
    position: absolute; left: 30px; top: 108px; width: 620px; height: 196px;
    border: 3px solid var(--blue); border-radius: 22px; padding: 5px;
  }
  .hero .photo { width: 100%; height: 100%; border-radius: 16px; }
  .headline { position: absolute; top: 314px; left: 0; width: 100%; text-align: center; }
  .headline-lead { font-size: 14px; line-height: 1.3; }
  .headline-main {
    font-family: "Montserrat", sans-serif; font-weight: 700;
    font-size: 32px; color: var(--blue); letter-spacing: .5px; line-height: 1.15;
  }
  .service { position: absolute; width: 275px; text-align: center; }
  .service-frame {
    height: 80px; border: 2px solid var(--teal); border-right-color: var(--blue);
    border-bottom-color: var(--blue); border-radius: 14px; padding: 4px;
  }
  .service-frame .photo { width: 100%; height: 100%; border-radius: 10px; }
  .service-title {
    margin-top: 5px; font-family: "Montserrat", sans-serif; font-weight: 600;
    font-size: 15px; color: var(--teal); letter-spacing: 1px; text-transform: uppercase; line-height: 1.2;
  }
  .service-sub { font-size: 11px; color: var(--muted); line-height: 1.3; }
  .s-einzel    { left: 40px;  top: 408px; }
  .s-paar      { left: 365px; top: 384px; }
  .s-familie   { left: 365px; top: 516px; }
  .s-erziehung { left: 40px;  top: 540px; }
  .costs { position: absolute; left: 40px; top: 670px; width: 600px; }
  .costs-title {
    font-family: "Montserrat", sans-serif; font-weight: 700; font-size: 19px;
    color: var(--teal); letter-spacing: 1px; line-height: 1.2;
  }
  .costs-title::before {
    content: ""; display: inline-block; width: 9px; height: 15px;
    background: var(--muted); margin-right: 8px; vertical-align: -1px;
  }
  .costs-intro { margin-top: 3px; font-size: 12.5px; line-height: 1.35; padding-left: 17px; }
  .prices {
    position: absolute; left: 40px; top: 736px; width: 600px; height: 164px;
    border: 2px solid var(--teal); border-radius: 16px; overflow: hidden;
    display: grid; grid-template-columns: 1fr 1fr; font-size: 10.5px;
    box-shadow: 0 2px 6px rgba(0,0,0,.12);
  }
  .price-col { display: grid; grid-template-rows: 36px 36px 1fr; }
  .price-col + .price-col { border-left: 1px solid var(--divider); }
  .price-row { padding: 4px 12px; display: flex; align-items: center; line-height: 1.35; }
  .price-row:nth-child(odd) { background: var(--row-grey); }
  .price-row b { font-weight: 700; font-family: "Montserrat", sans-serif; font-size: 10px; }
  .address-tab {
    position: absolute; right: 0; top: 906px; width: 300px; height: 24px;
    background: var(--blue); border-top-left-radius: 14px;
    color: #fff; font-size: 12px; display: flex; align-items: center; padding-left: 18px; gap: 6px;
  }
  .contact-band {
    position: absolute; left: 0; bottom: 0; width: 100%; height: 32px;
    background: var(--teal); color: #fff; display: flex; align-items: center;
    padding: 0 24px; gap: 40px; font-size: 13px;
  }
  .contact-item { display: flex; align-items: center; gap: 6px; }
  .phone-number { font-family: "Montserrat", sans-serif; font-weight: 600; font-size: 15px; }
  svg.icon { width: 13px; height: 13px; fill: #fff; }
</style>
</head>
<body>
  <main class="flyer">
    <header class="brand">
      <span class="brand-mark"></span>
      <div class="brand-name">Brigitte Volkanter</div>
      <div class="brand-sub">Familienberatung Lindenhof</div>
    </header>

    <div class="hero">
      <div class="photo" role="img" aria-label="Foto: Beratungsgespräch mit einer Familie im hellen Praxisraum"></div>
    </div>

    <section class="headline">
      <p class="headline-lead">Ist Ihr Leben an einem Punkt angekommen der</p>
      <h1 class="headline-main">VERÄNDERUNG BEDARF?</h1>
    </section>

    <article class="service s-einzel">
      <div class="service-frame"><div class="photo" role="img" aria-label="Foto: Beraterin am Flipchart in der Einzelberatung"></div></div>
      <h2 class="service-title">Einzelberatung</h2>
      <p class="service-sub">Eigenmächtig aus der Krise</p>
    </article>
    <article class="service s-paar">
      <div class="service-frame"><div class="photo" role="img" aria-label="Foto: Paar im Gespräch im Beratungsraum"></div></div>
      <h2 class="service-title">Paarberatung</h2>
      <p class="service-sub">Basis und Neubeginn</p>
    </article>
    <article class="service s-familie">
      <div class="service-frame"><div class="photo" role="img" aria-label="Foto: Mutter liest mit Kindern ein Buch"></div></div>
      <h2 class="service-title">Familie &amp; Kinder</h2>
      <p class="service-sub">Gemeinsam leben</p>
    </article>
    <article class="service s-erziehung">
      <div class="service-frame"><div class="photo" role="img" aria-label="Foto: Kinder beim gemeinsamen Spielen"></div></div>
      <h2 class="service-title">Erziehungsberatung</h2>
      <p class="service-sub">leiten – führen – begleiten</p>
    </article>

    <section class="costs">
      <h2 class="costs-title">KOSTEN:</h2>
      <p class="costs-intro">Ich begleite Sie auf Ihrem Weg: Es ist nie zu früh und selten zu spät, um Veränderungen zu setzen, die sich positiv auf Ihr Leben auswirken.</p>
    </section>

    <div class="prices">
      <div class="price-col">
        <div class="price-row"><span>Einzelberatung pro Stunde <b>€ 70</b></span></div>
        <div class="price-row"><span>Educational counseling per hour <b>€ 70</b></span></div>
        <div class="price-row"><span>Parental counseling according to <b>§ 95 Abs. 1a AussStrG</b><br>For couples per person <b>€ 30</b> or individual consultation <b>€ 60</b></span></div>
      </div>
      <div class="price-col">
        <div class="price-row"><span>Couple counseling per 1 ½ hours <b>€ 100</b></span></div>
        <div class="price-row"><span>Family counseling per 1 ½ hours <b>€ 100</b></span></div>
        <div class="price-row"><span>Family, parenting or educational counseling according to <b>§ 107 Abs. 3 Z 1 AussStrG</b><br>For couples per person <b>€ 45</b> or individual consultation <b>€ 80</b></span></div>
      </div>
    </div>

    <div class="address-tab">
      <svg class="icon" viewBox="0 0 24 24" aria-hidden="true"><path d="M12 2a7 7 0 0 0-7 7c0 5 7 13 7 13s7-8 7-13a7 7 0 0 0-7-7zm0 9.5A2.5 2.5 0 1 1 12 6.5a2.5 2.5 0 0 1 0 5z"/></svg>
      Lindengasse 14/3, 1220 Vienna
    </div>

    <footer class="contact-band">
      <span class="contact-item">
        <svg class="icon" viewBox="0 0 24 24" aria-hidden="true"><path d="M6.6 10.8a15 15 0 0 0 6.6 6.6l2.2-2.2a1 1 0 0 1 1-.25 11.4 11.4 0 0 0 3.6.57 1 1 0 0 1 1 1V20a1 1 0 0 1-1 1A17 17 0 0 1 3 4a1 1 0 0 1 1-1h3.5a1 1 0 0 1 1 1c0 1.25.2 2.45.57 3.57a1 1 0 0 1-.25 1z"/></svg>
        <span class="phone-number">+43 676 000 12 34</span>
      </span>
      <span class="contact-item">
        <svg class="icon" viewBox="0 0 24 24" aria-hidden="true"><path d="M2 5h20v14H2zm2 2v.5l8 5 8-5V7z"/></svg>
        familienberatung@brigitte-volkanter.at
      </span>
    </footer>
  </main>
</body>
</html>
```